Healthcare Service Provider looking for PowerPoint Template

VRM Profile of the company & business activity
===================================
VRM is the leading after-sale healthcare services provider in Kuwait. The IT department in the company sells & executes Healthcare IT projects in hospitals that mainly cover:

1. IT Infrastructure covering data center, disaster recovery, servers, virtualization, backup, redundancy & high-availability, multi-site connectivity, wired & wireless networking, OS & network management, software subscriptions, …etc.

2. Healthcare IT systems covering the Hospital Management system, Electronic Medical Record, evidence-based clinical content, clinical decision support systems, Radiology information system, Lab information system, pharmacy management system, ICU system, dental system, dietary & nutrition system, integration with 3rd party systems in the hospital

3. Human resources covering the company specialized teams of clinical informatics specialists, pharmacists, nurses, project managers, user experience specialists, integration specialists, systems analysts, systems developers, DB administrators, Network administrators, system architects, systems engineers, …

The assortment of these professionals handle the services for implementing specialty Healthcare IT systems, training hospital staff & healthcare professionals, on-site support & maintenance of implemented healthcare systems at the hospital

Requested design job
================
We require a PowerPoint template to be used by the IT department in presenting sales & marketing pitches, commercial proposals, projects, and related to the business activities described in the profile.

The design of the PowerPoint template should:

. be personalized for the business activities of the IT department. promote the corporate brand identity of the company. provide clean, modern and fluent look & feel for presenting on screen, projector or printing. include font selection & design as part of the template design. light colored background

. multiple page layouts & slide types like a cover slide, title slide, different types of content slides, ….

. include design collaterals like icons and clip-arts

. have common design elements in PowerPoint Master slides

Included are the current corporate logos of the company.

In summary, simplicity, fluency and personality are key to the design we seek.

Requirements
Must have
• The design of the PowerPoint template should:
• . be personalized for the business activities of the IT department. promote the corporate brand identity of the company. provide clean, modern and fluent look & feel for presenting on screen, projector or printing. include font selection & design as part of the template design. light colored background
• . multiple page layouts & slide types like a cover slide, title slide, different types of content slides, ….
• . include design collaterals like icons and clip-arts
• . have common design elements in PowerPoint Master slides

```html
<!DOCTYPE html>
<html lang="en">
<head>
<meta charset="utf-8">
<title>VRM Presentation Template</title>
<link href="https://fonts.googleapis.com/css2?family=Montserrat:wght@300;400;500;700&family=Cairo:wght@400;700&display=swap" rel="stylesheet">
<style>
  :root{
    --navy:#0b2440;
    --teal:#21a48d;
    --sky:#6cc8f0;
    --mist:#e3e6ea;
    --white:#ffffff;
    --ink:#1f3550;
    --bg-edge:#d9dadc;
  }
  *{box-sizing:border-box;margin:0;padding:0}
  html,body{width:1200px;height:1200px;overflow:hidden}
  body{
    position:relative;
    font-family:"Montserrat",sans-serif;
    background:radial-gradient(ellipse at 50% 45%, #ffffff 0%, #f4f4f5 55%, var(--bg-edge) 100%);
  }
  .slide{position:absolute;width:579px;height:434px;overflow:hidden;box-shadow:0 6px 18px rgba(0,0,0,.18)}
  .slide--cover{left:67px;top:59px;background:var(--navy)}
  .slide--content{left:395px;top:313px;background:var(--white)}
  .slide--closing{left:569px;top:727px;background:var(--navy)}

  .wordmark{position:absolute;color:var(--white);font-weight:700;letter-spacing:2px}
  .company{position:absolute;color:var(--white);font-weight:400;font-size:12.5px;white-space:nowrap}
  .company small{font-size:7px}
  .company-ar{position:absolute;color:var(--white);font-family:"Cairo",sans-serif;font-weight:700;font-size:14px;direction:rtl;white-space:nowrap}
  .company-ar small{font-weight:400;font-size:8px}

  /* cover */
  .cover__logo{left:93px;top:46px;font-size:44px}
  .cover__company{left:36px;top:114px}
  .cover__company-ar{left:36px;top:128px}
  .cover__visual{position:absolute;left:333px;top:0;width:246px;height:234px}
  .cover__headline{position:absolute;left:34px;top:205px;color:var(--white);font-size:14px;font-weight:400;line-height:1}
  .cover__headline .line{display:block;padding-bottom:4px;border-bottom:1px solid rgba(255,255,255,.7);white-space:nowrap}
  .cover__headline .line + .line{margin-top:10px;display:inline-block}
  .cover__headline b{font-weight:700;font-size:18px}
  .cover__headline .big{font-size:20px;font-weight:400}
  .cover__headline .mid{font-size:16px}

  .pillar{position:absolute;text-align:center}
  .pillar__hex{display:block;margin:0 auto}
  .pillar__title{font-weight:400;letter-spacing:.3px;line-height:1}
  .pillar__sub{font-size:5.5px;letter-spacing:.8px;line-height:1;margin-top:2px}
  .cover .pillar{width:90px;top:304px}
  .cover .pillar__title{color:var(--white);font-size:12px;margin-top:6px}
  .cover .pillar__sub{color:var(--white)}

  /* content slide */
  .content__header{position:absolute;left:0;top:0;width:100%;height:71px;background:var(--navy)}
  .content__title{position:absolute;left:25px;top:28px;color:var(--white);font-weight:300;font-size:19px;letter-spacing:.5px}
  .content .pillar{width:120px;top:102px}
  .content .pillar__title{color:var(--ink);font-size:12.5px;margin-top:4px}
  .content .pillar__sub{color:var(--ink);font-size:6px}
  .pillar__text{margin-top:16px;color:var(--ink);font-size:8.6px;line-height:11.6px;font-weight:400}
  .divider{position:absolute;top:118px;width:1px;height:224px;background:var(--ink)}
  .content__footer{position:absolute;left:0;top:394px;width:100%;height:13px;background:var(--navy)}
  .footer__mark{position:absolute;left:28px;top:382px;width:84px;height:36px;background:var(--white);border-radius:50%;
    display:flex;align-items:center;justify-content:center;color:var(--navy);font-weight:700;font-size:18px;letter-spacing:1px}
  .page-num{position:absolute;left:521px;top:392px;width:19px;height:17px;border-radius:50%;background:var(--white);
    color:var(--navy);font-size:9px;display:flex;align-items:center;justify-content:center}

  /* closing */
  .closing__logo{left:0;width:100%;top:132px;text-align:center;font-size:96px;letter-spacing:6px}
  .closing__company{left:0;width:100%;top:296px;text-align:center;font-size:17px}
  .closing__company small{font-size:9px}
  .closing__company-ar{left:0;width:100%;top:316px;text-align:center;font-size:20px}
  .closing__company-ar small{font-size:10px}
  .closing__rule{position:absolute;left:195px;width:340px;height:1px;background:linear-gradient(90deg,transparent,rgba(255,255,255,.8),transparent)}
  .closing__thanks{position:absolute;left:0;width:100%;top:371px;text-align:center;color:var(--white);font-weight:300;font-size:19px;letter-spacing:14px;padding-left:14px}
</style>
</head>
<body>

<svg width="0" height="0" style="position:absolute" aria-hidden="true">
  <defs>
    <symbol id="icon-data" viewBox="0 0 40 40">
      <g fill="none" stroke="currentColor" stroke-width="2.2" stroke-linecap="round">
        <ellipse cx="20" cy="12" rx="8" ry="3.2"/>
        <path d="M12 12v15c0 1.8 3.6 3.2 8 3.2s8-1.4 8-3.2V12"/>
        <path d="M12 17c0 1.8 3.6 3.2 8 3.2s8-1.4 8-3.2M12 22c0 1.8 3.6 3.2 8 3.2s8-1.4 8-3.2"/>
        <path d="M6 20a14 14 0 0 1 22-11.5M34 20a14 14 0 0 1-22 11.5"/>
        <path d="M28 4.5l.5 4.5-4.5.5M12 35.5l-.5-4.5 4.5-.5"/>
      </g>
    </symbol>
    <symbol id="icon-hospital" viewBox="0 0 40 40">
      <g fill="currentColor">
        <rect x="3" y="30" width="34" height="1.8"/>
        <path d="M13 9h14v21h-14zM6 17h7v13H6zM27 17h7v13h-7z" fill="none" stroke="currentColor" stroke-width="1.6"/>
        <g>
          <rect x="15" y="11" width="2" height="2"/><rect x="19" y="11" width="2" height="2"/><rect x="23" y="11" width="2" height="2"/>
          <rect x="15" y="15" width="2" height="2"/><rect x="19" y="15" width="2" height="2"/><rect x="23" y="15" width="2" height="2"/>
          <rect x="15" y="19" width="2" height="2"/><rect x="19" y="19" width="2" height="2"/><rect x="23" y="19" width="2" height="2"/>
          <rect x="18" y="24" width="4" height="6"/>
          <rect x="8" y="20" width="3" height="3"/><rect x="29" y="20" width="3" height="3"/>
          <rect x="8" y="25" width="3" height="3"/><rect x="29" y="25" width="3" height="3"/>
        </g>
      </g>
    </symbol>
    <symbol id="icon-people" viewBox="0 0 40 40">
      <g fill="none" stroke="currentColor" stroke-width="2.4" stroke-linecap="round">
        <path d="M7 22a13 13 0 0 1 22-11M33 18a13 13 0 0 1-22 11"/>
        <path d="M29 6l.3 5.2-5 .4M11 34l-.3-5.2 5-.4"/>
      </g>
      <circle cx="20" cy="16" r="3.6" fill="currentColor"/>
      <path d="M13.5 27c0-4.2 2.9-6.5 6.5-6.5s6.5 2.3 6.5 6.5z" fill="currentColor"/>
    </symbol>
    <symbol id="hex" viewBox="0 0 100 88">
      <polygon points="26,4 74,4 97,44 74,84 26,84 3,44" stroke-linejoin="round" stroke-width="6"/>
    </symbol>
  </defs>
</svg>

<!-- Cover slide -->
<section class="slide slide--cover cover">
  <div class="wordmark cover__logo">VRM</div>
  <div class="company cover__company">Vertex Regional Medtech <small>K.S.C.P.</small></div>
  <div class="company-ar cover__company-ar"><small>ش.م.ك.ع</small> شركة فيرتكس الإقليمية</div>

  <svg class="cover__visual" viewBox="0 0 246 234" role="img" aria-label="Healthcare technology photo: hand touching a digital interface of medical icons, shown through diagonal rounded bands">
    <defs>
      <linearGradient id="visual-tone" x1="0" y1="0" x2="1" y2="1">
        <stop offset="0" stop-color="#bfe6f7"/>
        <stop offset=".5" stop-color="#eaf6fc"/>
        <stop offset="1" stop-color="#d9e7ef"/>
      </linearGradient>
    </defs>
    <g stroke="url(#visual-tone)" stroke-linecap="round" stroke-width="34">
      <line x1="-45" y1="210" x2="135" y2="30"/>
      <line x1="30" y1="50" x2="125" y2="-45"/>
      <line x1="70" y1="180" x2="250" y2="0"/>
      <line x1="160" y1="215" x2="280" y2="95"/>
    </g>
    <g stroke="#50bde8" stroke-linecap="round" stroke-width="34" opacity=".55">
      <line x1="-20" y1="185" x2="75" y2="90"/>
      <line x1="40" y1="40" x2="90" y2="-10"/>
    </g>
  </svg>

  <h1 class="cover__headline">
    <span class="line"><b>VRM</b> IS THE <span class="big">LEADING</span> AFTER-SALE <b>HEALTHCARE</b></span>
    <span class="line"><span class="mid">SERVICES PROVIDER IN</span> <span class="big">KUWAIT</span></span>
  </h1>

  <div class="pillar" style="left:32px">
    <svg class="pillar__hex" width="80" height="70" viewBox="0 0 100 88"><use href="#hex" fill="var(--teal)" stroke="var(--teal)"/><use href="#icon-data" x="26" y="20" width="48" height="48" style="color:#fff"/></svg>
    <div class="pillar__title">COVERING</div><div class="pillar__sub">DATA</div>
  </div>
  <div class="pillar" style="left:130px">
    <svg class="pillar__hex" width="80" height="70" viewBox="0 0 100 88"><use href="#hex" fill="#fff" stroke="#fff"/><use href="#icon-hospital" x="24" y="18" width="52" height="52" style="color:var(--navy)"/></svg>
    <div class="pillar__title">HOSPITAL</div><div class="pillar__sub">MANAGEMENT</div>
  </div>
  <div class="pillar" style="left:229px">
    <svg class="pillar__hex" width="80" height="70" viewBox="0 0 100 88"><use href="#hex" fill="var(--sky)" stroke="var(--sky)"/><use href="#icon-people" x="26" y="20" width="48" height="48" style="color:var(--navy)"/></svg>
    <div class="pillar__title">HUMAN</div><div class="pillar__sub">RESOURCES</div>
  </div>
</section>

<!-- Content slide -->
<section class="slide slide--content content">
  <div class="content__header"></div>
  <h2 class="content__title">PRESENTATION TITLE</h2>

  <div class="pillar" style="left:67px">
    <svg class="pillar__hex" width="84" height="74" viewBox="0 0 100 88"><use href="#hex" fill="var(--teal)" stroke="var(--teal)"/><use href="#icon-data" x="26" y="20" width="48" height="48" style="color:#fff"/></svg>
    <div class="pillar__title">COVERING</div><div class="pillar__sub">DATA</div>
    <p class="pillar__text">IT Infrastructure covering data center, disaster recovery, servers, virtualization, backup, redundancy &amp; high-availability, multi-site connectivity, wired &amp; wireless networking, OS &amp; network management, software subscriptions, ....etc</p>
  </div>
  <div class="divider" style="left:205px"></div>
  <div class="pillar" style="left:232px;width:130px">
    <svg class="pillar__hex" width="84" height="74" viewBox="0 0 100 88"><use href="#hex" fill="var(--mist)" stroke="var(--mist)"/><use href="#icon-hospital" x="24" y="18" width="52" height="52" style="color:var(--navy)"/></svg>
    <div class="pillar__title">HOSPITAL</div><div class="pillar__sub">MANAGEMENT</div>
    <p class="pillar__text">Healthcare IT systems covering the Hospital Management system, Electronic Medical Record, evidence-based clinical content, clinical decision support systems, Radiology information system, Lab information system, pharmacy management system, ICU</p>
  </div>
  <div class="divider" style="left:383px"></div>
  <div class="pillar" style="left:401px">
    <svg class="pillar__hex" width="84" height="74" viewBox="0 0 100 88"><use href="#hex" fill="var(--sky)" stroke="var(--sky)"/><use href="#icon-people" x="26" y="20" width="48" height="48" style="color:var(--navy)"/></svg>
    <div class="pillar__title">HUMAN</div><div class="pillar__sub">RESOURCES</div>
    <p class="pillar__text">Human resources covering the company specialized teams of clinical informatics specialists, pharmacists, nurses, project managers, user experience specialists, integration specialists, systems analysts, systems developers, DB</p>
  </div>

  <div class="content__footer"></div>
  <div class="footer__mark">VRM</div>
  <div class="page-num">1</div>
</section>

<!-- Closing slide -->
<section class="slide slide--closing">
  <div class="wordmark closing__logo">VRM</div>
  <div class="company closing__company">Vertex Regional Medtech <small>K.S.C.P.</small></div>
  <div class="company-ar closing__company-ar"><small>ش.م.ك.ع</small> شركة فيرتكس الإقليمية</div>
  <div class="closing__rule" style="top:366px"></div>
  <div class="closing__thanks">THANK YOU</div>
  <div class="closing__rule" style="top:397px"></div>
</section>

</body>
</html>
```